Business card/Stationary for mobile ultrasound company
Corvin Ultrasound Services, LLC
Business card/Stationary for mobile ultrasound company -
Creative Brief
Use specific fonts
can use a combination of fonts similar to logo
Professional
Tessa Quillon RDMS, RVT, RCS
Owner
P.O. Box 482 Dunmore Flats, NM 88099-0482
4quillons@mailnest.example
I am currently getting a website designed so i will add a web address and an updated email address specifically for the business. I am torn as to use a one sided or 2 sided card. So im open. I would rather not have the address on the card. Thanks
Innovative mobile technology focused on improving the QUALITY of patient care. (The wording can change but along this idea)

```html
<!DOCTYPE html>
<html lang="en">
<head>
<meta charset="utf-8">
<title>Corvin Ultrasound Services – Business Card</title>
<link rel="stylesheet" href="https://fonts.googleapis.com/css2?family=Lato:ital,wght@0,400;0,700;1,400;1,700&display=swap">
<style>
  :root {
    --backdrop: #d9d9d9;
    --card-white: #ffffff;
    --card-black: #0b0b0b;
    --accent-light: #e4e4e4;
    --accent-dark: #8a8a8a;
    --ink: #1c1c1c;
    --ink-soft: #3a3a3a;
    --logo-ink: #f2f2f2;
  }
  * { margin: 0; padding: 0; box-sizing: border-box; }
  html, body {
    width: 1200px;
    height: 780px;
    overflow: hidden;
    background: var(--backdrop);
    font-family: "Lato", Arial, sans-serif;
  }
  .canvas {
    position: relative;
    width: 1200px;
    height: 780px;
  }
  .business-card {
    position: absolute;
    left: 75px;
    top: 90px;
    width: 1050px;
    height: 600px;
    border-radius: 34px;
    overflow: hidden;
    background: var(--card-white);
    box-shadow: 0 10px 30px rgba(0,0,0,0.18);
  }
  .card-shapes {
    position: absolute;
    inset: 0;
  }
  .contact-block {
    position: absolute;
    left: 56px;
    color: var(--ink);
  }
  .person {
    top: 150px;
  }
  .person-name {
    font-size: 23px;
    font-weight: 700;
    font-style: italic;
  }
  .person-credentials {
    font-size: 16px;
    font-weight: 700;
    font-style: italic;
    margin-left: 5px;
  }
  .person-role {
    margin-top: 10px;
    font-size: 20px;
    font-style: italic;
    color: var(--ink-soft);
  }
  .mailing-address {
    top: 355px;
    font-size: 20px;
    font-style: normal;
    line-height: 31px;
    color: var(--ink-soft);
  }
  .reach {
    top: 458px;
    font-size: 20px;
    color: var(--ink-soft);
  }
  .reach-line {
    display: flex;
    align-items: center;
    gap: 14px;
    height: 40px;
  }
  .reach-icon {
    width: 22px;
    height: 22px;
    flex: none;
  }
  .reach-at {
    width: 22px;
    font-size: 23px;
    font-weight: 700;
    color: var(--ink);
    text-align: center;
    line-height: 1;
  }
  .brand-name {
    position: absolute;
    left: 560px;
    top: 215px;
    width: 420px;
    text-align: center;
    color: var(--logo-ink);
    font-weight: 400;
  }
  .brand-main {
    display: block;
    font-size: 74px;
    letter-spacing: 2px;
    line-height: 1;
  }
  .brand-sub {
    display: block;
    margin-top: 10px;
    font-size: 24px;
    letter-spacing: 1px;
  }
</style>
</head>
<body>
<main class="canvas">
  <section class="business-card" aria-label="Business card for Corvin Ultrasound Services, LLC">
    <svg class="card-shapes" viewBox="0 0 1050 600" width="1050" height="600" aria-hidden="true">
      <defs>
        <linearGradient id="accentGradient" x1="0" y1="0" x2="0" y2="1">
          <stop offset="0" stop-color="var(--accent-dark)"/>
          <stop offset="0.5" stop-color="var(--accent-light)"/>
          <stop offset="1" stop-color="var(--accent-dark)"/>
        </linearGradient>
      </defs>
      <path class="accent-band" fill="url(#accentGradient)"
            d="M388 0 C330 130 330 230 380 320 C430 410 520 480 548 600 L1050 600 L1050 0 Z"/>
      <path class="dark-panel" fill="var(--card-black)"
            d="M404 0 C348 130 348 228 398 314 C448 400 540 470 570 600 L1050 600 L1050 0 Z"/>
    </svg>

    <div class="contact-block person">
      <p><span class="person-name">Tessa Quillon</span><span class="person-credentials">RDMS, RVT, RCS</span></p>
      <p class="person-role">Owner</p>
    </div>

    <address class="contact-block mailing-address">
      P.O. Box 482<br>
      Dunmore Flats, NM 88099-0482
    </address>

    <div class="contact-block reach">
      <p class="reach-line">
        <svg class="reach-icon" viewBox="0 0 24 24" aria-hidden="true">
          <path fill="var(--ink)" d="M6.6 10.8c1.4 2.8 3.8 5.1 6.6 6.6l2.2-2.2c.3-.3.7-.4 1-.2 1.1.4 2.3.6 3.6.6.6 0 1 .4 1 1V20c0 .6-.4 1-1 1C10.6 21 3 13.4 3 4c0-.6.4-1 1-1h3.5c.6 0 1 .4 1 1 0 1.3.2 2.5.6 3.6.1.3 0 .7-.2 1L6.6 10.8z"/>
        </svg>
        <span>575-555-0148</span>
      </p>
      <p class="reach-line">
        <span class="reach-at" aria-hidden="true">@</span>
        <span>4quillons@mailnest.example</span>
      </p>
    </div>

    <p class="brand-name">
      <span class="brand-main">Corvin</span>
      <span class="brand-sub">Ultrasound Services, LLC</span>
    </p>
  </section>
</main>
</body>
</html>
```